Business Card Design

I am a Special Event Consultant,I arrange and organise Special Events - Product Launches,Sponsorship and Product Displays.

I would like the RTV to be a feature of the design with 'Special Event Services" underneath - keep it very simple but creative using this information. So it is just the letters "RTV" with Event Services underneath.

(Simple Colours - Silver, Black, Grey - no bright colours - We work for Valtoria Drenn,KDX, Lyndrel So it is class and classic.)

Only my Name and mobile on the front.

Contact Information for Business Card

FRONT
Tess Varnholt
Tel: 0436 218907

BACK
Email: tess@rtveventservices.example.au

2807 Wexbury Heights,83 Pollard Street
NORTHVALE.Vic.3158.

```html
<!DOCTYPE html>
<html lang="en">
<head>
<meta charset="utf-8">
<title>RTV Event Services – Business Card</title>
<link rel="stylesheet" href="https://fonts.googleapis.com/css2?family=Josefin+Sans:wght@300;400&display=swap">
<style>
  :root {
    --backdrop: #e4e4e4;
    --charcoal: #2a2a2c;
    --silver: #c4c6c9;
    --silver-light: #e6e7e9;
    --card-white: #ffffff;
    --ink: #1a1a1a;
    --rule: #555555;
    --footer-band: #efefef;
    --footer-ink: #444444;
  }
  * { margin: 0; padding: 0; box-sizing: border-box; }
  html, body {
    width: 1200px; height: 800px; overflow: hidden;
    background: var(--backdrop);
    font-family: "Josefin Sans", sans-serif;
  }
  .canvas { position: relative; width: 1200px; height: 800px; }

  .card {
    position: absolute; top: 265px; width: 539px; height: 292px;
    border-radius: 4px; overflow: hidden;
    box-shadow: 0 2px 4px rgba(0,0,0,0.25);
  }
  .card-back { left: 45px; background: var(--charcoal); }
  .card-front { left: 601px; background: var(--card-white); }

  .card-back .edge-strip {
    position: absolute; left: 0; top: 0; width: 29px; height: 100%;
    background: var(--silver);
  }
  .card-front .edge-strip {
    position: absolute; left: 0; top: 0; width: 28px; height: 100%;
    background: var(--charcoal);
  }

  .brand-mark {
    position: absolute; left: 55px; top: 38px; color: var(--silver);
  }
  .brand-name {
    font-size: 34px; font-weight: 300; letter-spacing: 8px; line-height: 34px;
  }
  .brand-tagline {
    margin-top: 4px; font-size: 9px; font-weight: 400; letter-spacing: 2.4px;
    text-transform: uppercase; color: var(--silver-light);
  }

  .contact-row { position: absolute; display: flex; align-items: flex-start; color: var(--silver-light); }
  .contact-icon { width: 28px; height: 28px; flex: none; }
  .contact-text {
    font-size: 15px; font-weight: 300; line-height: 16.5px;
    text-transform: uppercase; letter-spacing: 0.3px;
  }
  .address-row { left: 54px; top: 118px; }
  .address-row .contact-text { margin-left: 15px; margin-top: 3px; }
  .email-row { left: 53px; top: 197px; }
  .email-row .contact-text { margin-left: 15px; margin-top: 8px; font-size: 14px; letter-spacing: 0; }

  .holder-name {
    position: absolute; left: 38px; top: 96px;
    font-size: 24px; font-weight: 300; color: var(--ink);
    letter-spacing: 0.6px; text-transform: uppercase;
  }
  .holder-role {
    position: absolute; left: 38px; top: 125px; width: 468px;
    display: flex; align-items: center;
    font-size: 9px; font-weight: 400; color: var(--ink);
    letter-spacing: 0.6px; text-transform: uppercase;
  }
  .holder-role::after {
    content: ""; flex: 1; height: 1px; background: var(--rule); margin-left: 5px; margin-top: -2px;
  }
  .mobile-row {
    position: absolute; left: 47px; top: 195px;
    display: flex; align-items: center; color: var(--ink);
  }
  .mobile-row svg { width: 18px; height: 18px; }
  .mobile-number { margin-left: 13px; font-size: 17px; font-weight: 300; letter-spacing: 1px; margin-top: 3px; }

  .footer-band {
    position: absolute; left: 28px; right: 0; bottom: 0; height: 24px;
    background: var(--footer-band);
    display: flex; align-items: center; justify-content: flex-end; padding-right: 19px;
    font-size: 8.5px; letter-spacing: 0.6px; color: var(--footer-ink); text-transform: uppercase;
  }
</style>
</head>
<body>
<div class="canvas">

  <section class="card card-back" aria-label="Card back">
    <div class="edge-strip"></div>
    <div class="brand-mark">
      <p class="brand-name">RTV</p>
      <p class="brand-tagline">Special Event Services</p>
    </div>
    <div class="contact-row address-row">
      <svg class="contact-icon" viewBox="0 0 28 28" aria-hidden="true">
        <circle cx="14" cy="14" r="12" fill="none" stroke="var(--silver-light)" stroke-width="2"/>
        <path d="M14 7.5a4.5 4.5 0 0 0-4.5 4.5c0 3.3 4.5 8.5 4.5 8.5s4.5-5.2 4.5-8.5A4.5 4.5 0 0 0 14 7.5z" fill="var(--silver-light)"/>
        <circle cx="14" cy="12" r="1.7" fill="var(--charcoal)"/>
      </svg>
      <p class="contact-text">2807 Wexbury Heights<br>83 Pollard Street<br>Northvale.Vic.3158</p>
    </div>
    <div class="contact-row email-row">
      <svg class="contact-icon" viewBox="0 0 28 28" aria-hidden="true">
        <circle cx="14" cy="14" r="12" fill="none" stroke="var(--silver-light)" stroke-width="2"/>
        <rect x="7.5" y="9.5" width="13" height="9" rx="1" fill="var(--silver-light)"/>
        <path d="M8 10l6 4.5 6-4.5" fill="none" stroke="var(--charcoal)" stroke-width="1.2"/>
      </svg>
      <p class="contact-text">tess@rtveventservices.example.au</p>
    </div>
  </section>

  <section class="card card-front" aria-label="Card front">
    <div class="edge-strip"></div>
    <h1 class="holder-name">Tess Varnholt</h1>
    <p class="holder-role">Event Consultant</p>
    <div class="mobile-row">
      <svg viewBox="0 0 18 18" aria-hidden="true">
        <circle cx="9" cy="9" r="8" fill="none" stroke="#999" stroke-width="0.8"/>
        <path d="M6.2 4.6l1.5 2.1-1 1c.6 1.3 1.5 2.2 2.7 2.8l1-1 2.1 1.5-.8 1.6c-3.3-.4-5.9-3-6.3-6.3z" fill="#222"/>
      </svg>
      <span class="mobile-number">0436 218907</span>
    </div>
    <div class="footer-band">Special Event Services</div>
  </section>

</div>
</body>
</html>
```